Business card - Harbourline Stoneworks

Design a business card utilizing the given logo.
colors we like: Black, greys, Teal, blues.
Tri color card, horizontal orientation likely
Logo and name likely best on top.
Info on card:

Dennis Farrowby
#5 - 4180 Maple Ridge Blvd.
Surrey, B.C. V3K 2R9

778.555.0193
dennisfarrowby@brellnet.ca

Slogan: "Building Dreams"

We are a construction company that specializes in new home construction on the West coast of BC Canada. Open Concepts designs of high end homes.

```html
<!DOCTYPE html>
<html lang="en">
<head>
<meta charset="utf-8">
<title>Harbourline Stoneworks – Business Card</title>
<link rel="stylesheet" href="https://fonts.googleapis.com/css2?family=Questrial&family=Montserrat:wght@600&display=swap">
<style>
  :root {
    --canvas: #d9d9d6;
    --card-dark: #3b3b3d;
    --card-dark-edge: #2e2e30;
    --card-light: #ffffff;
    --ink: #1c1c1c;
    --ink-soft: #3a3a3a;
    --swoosh: #0b0b0b;
    --teal: #1f8f9c;
    --teal-deep: #17707b;
    --mark: #1c1c1c;
    --mark-on-dark: #111111;
  }
  * { margin: 0; padding: 0; box-sizing: border-box; }
  html, body { width: 1200px; height: 871px; overflow: hidden; }
  body {
    background: var(--canvas);
    font-family: "Questrial", "Century Gothic", sans-serif;
    color: var(--ink);
    position: relative;
  }
  .card {
    position: absolute;
    left: 290px;
    width: 620px;
    height: 354px;
    overflow: hidden;
    box-shadow: 0 10px 24px rgba(0,0,0,.25);
  }
  .card-back { top: 60px; background: linear-gradient(160deg, var(--card-dark) 0%, var(--card-dark-edge) 100%); }
  .card-front { top: 457px; background: var(--card-light); }
  .card-edge { position: absolute; inset: 0; width: 100%; height: 100%; }

  .brand {
    position: absolute;
    display: flex;
    align-items: center;
    gap: 12px;
    white-space: nowrap;
  }
  .brand-dot { width: 34px; height: 34px; border-radius: 50%; background: var(--mark); }
  .brand-name { font-size: 25px; letter-spacing: 1.5px; color: var(--mark); }
  .card-back .brand { left: 50%; top: 128px; transform: translateX(-50%); }
  .card-back .brand-dot { background: var(--mark-on-dark); }
  .card-back .brand-name { color: var(--mark-on-dark); }
  .card-front .brand { right: 40px; top: 70px; }

  .slogan {
    position: absolute;
    right: 58px;
    bottom: 10px;
    color: #e8f6f7;
    font-size: 14px;
    letter-spacing: 2px;
  }

  .holder { position: absolute; left: 48px; top: 140px; }
  .holder-name {
    font-family: "Montserrat", "Century Gothic", sans-serif;
    font-weight: 600;
    font-size: 15px;
    letter-spacing: 2.5px;
    margin-bottom: 18px;
  }
  .holder-address { font-size: 12.5px; letter-spacing: 1.2px; line-height: 1.45; color: var(--ink-soft); }

  .contact { position: absolute; left: 300px; top: 198px; list-style: none; }
  .contact li {
    display: flex; align-items: center; gap: 14px;
    font-size: 13.5px; letter-spacing: 1.6px; color: var(--ink-soft);
    margin-bottom: 8px;
  }
  .contact svg { width: 13px; height: 13px; flex: none; }
</style>
</head>
<body>

<section class="card card-back" aria-label="Card back">
  <svg class="card-edge" viewBox="0 0 620 354" preserveAspectRatio="none" aria-hidden="true">
    <path d="M0,286 C180,300 420,292 620,255 L620,354 L0,354 Z" fill="var(--swoosh)"/>
    <path d="M0,300 C190,318 420,308 620,272 L620,354 L0,354 Z" fill="var(--teal)"/>
  </svg>
  <div class="brand">
    <span class="brand-dot"></span>
    <span class="brand-name">HARBOURLINE STONEWORKS</span>
  </div>
  <p class="slogan">Building Dreams</p>
</section>

<section class="card card-front" aria-label="Card front">
  <svg class="card-edge" viewBox="0 0 620 354" preserveAspectRatio="none" aria-hidden="true">
    <path d="M0,286 C200,320 430,330 620,318 L620,354 L0,354 Z" fill="var(--swoosh)"/>
    <path d="M0,300 C210,332 430,340 620,328 L620,354 L0,354 Z" fill="var(--teal)"/>
  </svg>
  <div class="brand">
    <span class="brand-dot"></span>
    <span class="brand-name">HARBOURLINE STONEWORKS</span>
  </div>

  <div class="holder">
    <p class="holder-name">Dennis Farrowby</p>
    <p class="holder-address">#5 - 4180 Maple Ridge Blvd.<br>Surrey, B.C. V3K 2R9</p>
  </div>

  <ul class="contact">
    <li>
      <svg viewBox="0 0 16 16" aria-hidden="true"><path d="M3 5c0-2 2-3 5-3s5 1 5 3l-2 1-1-2H6L5 6 3 5zM4 7h8l1 6H3l1-6zm4 1.5a2 2 0 100 4 2 2 0 000-4z" fill="var(--teal)"/></svg>
      <span>778.555.0193</span>
    </li>
    <li>
      <svg viewBox="0 0 16 16" aria-hidden="true"><rect x="1.5" y="3.5" width="13" height="9" fill="none" stroke="var(--teal)" stroke-width="1.5"/><path d="M1.5 3.5 8 9l6.5-5.5" fill="none" stroke="var(--teal)" stroke-width="1.5"/></svg>
      <span>dennisfarrowby@brellnet.ca</span>
    </li>
  </ul>
</section>

</body>
</html>
```